Logo alteration and design business card.

I want to make minor alterations to a logo that has already been designed and use the modified logo as part of the design of the business card.

Alterations to be made are as follows:
16-6240 TPX For the top green and bottom green dot.
16-4535 TPX For the Bottom blue and top blue dot
13-0220 TPX For the green outline.
13-5313 TPX For the middle line and the writing.

Particulars such as name, phone number and email to be generic for now so we can update and individualize them later. Website is www.orbalune.com.au

Target Market(s)

Men and Women 25-35 interested in ecofriendly/green products that have a positive vibe and message.

Industry/Entity Type

Business

Font styles to use
Script

Colors
0492cd
85cae6
00a98f
86cfc6

Requirements
Must have
• The modified Comet Hush logo.
Nice to have
• We're looking for a design that is either nature based eg. bamboo, birds, trees, water, natural scenery etc. or something eg. spacey, stars, galaxy, universe etc. a positive/happy feeling to it that is quite simple and not over loaded with imagery.

```html
<!DOCTYPE html>
<html lang="en">
<head>
<meta charset="utf-8">
<title>Comet Hush Business Card</title>
<link rel="stylesheet" href="https://fonts.googleapis.com/css2?family=Anton&family=Jost:wght@400;600&display=swap">
<style>
  :root {
    --page-bg: #e9ece8;
    --forest: #0b7a2f;
    --leaf: #2eac67;
    --mint-line: #b4e8a2;
    --aqua-text: #8fdcd6;
    --logo-blue: #0cb3d6;
    --scenery-canopy: #3fa33a;
    --scenery-moss: #1f7a2c;
    --scenery-shade: #0f4f24;
    --scenery-water: #5fae8e;
  }
  html, body {
    margin: 0;
    width: 1200px;
    height: 1000px;
    overflow: hidden;
    background: var(--page-bg);
  }
  .canvas {
    position: relative;
    width: 1200px;
    height: 1000px;
  }
  .card {
    position: absolute;
    left: 250px;
    width: 700px;
    height: 400px;
    border-radius: 28px;
    overflow: hidden;
    box-shadow: 0 6px 18px rgba(0,0,0,0.18);
  }
  .card--front { top: 70px; }
  .card--back { top: 530px; }
  .card svg { display: block; }
  .brand-title {
    font-family: "Anton", "Arial Narrow", sans-serif;
    font-size: 64px;
    fill: var(--aqua-text);
    letter-spacing: 1px;
  }
  .person-name {
    font-family: "Jost", "Futura", sans-serif;
    font-weight: 600;
    font-size: 26px;
    fill: var(--aqua-text);
  }
  .person-role {
    font-family: "Jost", "Futura", sans-serif;
    font-weight: 400;
    font-size: 23px;
    fill: var(--aqua-text);
  }
  .contact-line, .web-address {
    font-family: "Jost", "Futura", sans-serif;
    font-weight: 400;
    font-size: 22px;
    fill: var(--aqua-text);
  }
  .logo-name {
    font-family: "Jost", "Futura", sans-serif;
    font-weight: 400;
    font-size: 32px;
    fill: var(--aqua-text);
  }
  .icon { fill: none; stroke: var(--aqua-text); stroke-width: 1.6; }
</style>
</head>
<body>
<main class="canvas">

  <section class="card card--front">
    <svg width="700" height="400" viewBox="0 0 700 400">
      <defs>
        <radialGradient id="sceneryTones" cx="0.45" cy="0.75" r="0.75">
          <stop offset="0" stop-color="var(--scenery-water)"/>
          <stop offset="0.3" stop-color="var(--scenery-shade)"/>
          <stop offset="0.65" stop-color="var(--scenery-moss)"/>
          <stop offset="1" stop-color="var(--scenery-canopy)"/>
        </radialGradient>
      </defs>
      <rect class="front-base" width="700" height="400" fill="var(--forest)"/>
      <ellipse class="scenery-frame" cx="330" cy="140" rx="345" ry="250" fill="none" stroke="var(--mint-line)" stroke-width="8"/>
      <ellipse class="scenery-photo" cx="330" cy="140" rx="338" ry="243" fill="url(#sceneryTones)"
               role="img" aria-label="Photo of a mossy green gorge with a waterfall flowing into a calm pool"/>
      <g class="logo-mark">
        <circle cx="560" cy="235" r="88" fill="var(--logo-blue)"/>
        <text class="logo-name" x="560" text-anchor="middle">
          <tspan x="560" y="226">Comet</tspan>
          <tspan x="560" y="264">Hush</tspan>
        </text>
      </g>
    </svg>
  </section>

  <section class="card card--back">
    <svg width="700" height="400" viewBox="0 0 700 400">
      <rect class="back-base" width="700" height="400" fill="var(--leaf)"/>
      <path class="lower-band" d="M0 185 Q 300 320 700 338 L700 400 L0 400 Z" fill="var(--mint-line)"/>
      <path class="lower-band-fill" d="M0 199 Q 300 334 700 352 L700 400 L0 400 Z" fill="var(--forest)"/>

      <text class="brand-title" x="410" y="145" text-anchor="middle">COMET HUSH</text>
      <text class="person-name" x="410" y="190" text-anchor="middle">YOUR NAME</text>
      <text class="person-role" x="410" y="217" text-anchor="middle">YOUR PROFESSION</text>

      <g class="contact-list">
        <rect class="icon" x="40" y="276" width="10" height="17" rx="2"/>
        <text class="contact-line" x="62" y="293">12345678910</text>
        <g class="icon">
          <rect x="36" y="314" width="18" height="10" rx="1"/>
          <rect x="40" y="308" width="10" height="6"/>
        </g>
        <text class="contact-line" x="62" y="326">12345678910</text>
        <g class="icon">
          <rect x="36" y="346" width="18" height="12"/>
          <path d="M36 346 L45 353 L54 346"/>
        </g>
        <text class="contact-line" x="62" y="359">youremail@mailbox.com</text>
      </g>

      <text class="web-address" x="680" y="387" text-anchor="end">www.orbalune.com</text>
    </svg>
  </section>

</main>
</body>
</html>
```